Lumawerks Business Card Design

I need a business card design for a new Business, that is focused on Custom Made Designer Furniture. that is aimed at the mid to high end markets. I would like a card that would in some way portray what I do for my clients in the way we are able to make any idea a reality and also work within a set budget to meet their requirements.
I like quite contemporary colours and styling and I want the final design to communicate a Contemporary and Professional image.

Target Market(s)

mid to high end market

Industry/Entity Type

Business

Contact Information for Business Card

Lumawerks
Darren Holtzmann
18 Wexbury Rd, Kelston, Auckland, New Zealand 0712.

Requirements
Nice to have
• I would also like to utilize the spot gloss or raised print on my cards

```html
<!DOCTYPE html>
<html lang="en">
<head>
<meta charset="utf-8">
<title>Lumawerks Business Card</title>
<link href="https://fonts.googleapis.com/css2?family=Poiret+One&family=Open+Sans:wght@700&display=swap" rel="stylesheet">
<style>
  :root {
    --page: #ffffff;
    --panel-grey: #b3b3b3;
    --ornament-light: #cfcfcf;
    --ornament-dark: #5a5a5a;
    --stripe-black: #0d0d0d;
    --stripe-grey: #555555;
    --card-edge: #e4e4e4;
    --ink: #111111;
  }
  * { margin: 0; padding: 0; box-sizing: border-box; }
  html, body {
    width: 1200px;
    height: 741px;
    overflow: hidden;
    background: var(--page);
  }
  .card {
    position: absolute;
    left: 16px;
    top: 33px;
    width: 1165px;
    height: 677px;
    border: 1px solid var(--card-edge);
    background: var(--page);
  }
  .card__panel {
    position: absolute;
    left: 0;
    top: 0;
    width: 487px;
    height: 100%;
    background: var(--panel-grey);
  }
  .card__ornament {
    position: absolute;
    left: 80px;
    top: 10px;
    width: 407px;
    height: 655px;
    border-radius: 50% 0 0 50%;
    background: radial-gradient(ellipse at 70% 50%, var(--ornament-light) 0%, #9a9a9a 55%, var(--panel-grey) 80%);
  }
  .card__stripes {
    position: absolute;
    left: 487px;
    top: 0;
    width: 84px;
    height: 100%;
    display: block;
  }
  .card__info {
    position: absolute;
    left: 571px;
    top: 0;
    right: 0;
    height: 100%;
    text-align: center;
    color: var(--ink);
    font-family: "Poiret One", sans-serif;
  }
  .brand-name {
    position: absolute;
    left: 0; right: 0;
    top: 142px;
    font-size: 66px;
    line-height: 1;
    letter-spacing: 1px;
  }
  .person-name {
    position: absolute;
    left: 0; right: 0;
    top: 283px;
    font-size: 42px;
    font-variant: small-caps;
    line-height: 1;
  }
  .person-role {
    position: absolute;
    left: 0; right: 0;
    top: 333px;
    font-family: "Open Sans", sans-serif;
    font-weight: 700;
    font-size: 18px;
    line-height: 1;
  }
  .tagline {
    position: absolute;
    left: 0; right: 0;
    top: 399px;
    font-size: 25px;
    font-variant: small-caps;
    font-weight: 400;
    -webkit-text-stroke: 0.4px var(--ink);
    line-height: 1;
  }
  .address {
    position: absolute;
    left: 0; right: 0;
    top: 510px;
    font-style: normal;
    font-size: 22px;
    font-variant: small-caps;
    line-height: 29px;
  }
</style>
</head>
<body>
  <div class="card">
    <div class="card__panel">
      <div class="card__ornament" role="img" aria-label="Decorative flourish of scrolling leaves and swirls in dark and light grey"></div>
    </div>
    <svg class="card__stripes" viewBox="0 0 84 677" preserveAspectRatio="none" aria-hidden="true">
      <defs>
        <pattern id="band-stripes" width="84" height="15.2" patternUnits="userSpaceOnUse">
          <rect width="84" height="8.5" fill="var(--stripe-black)"/>
          <rect y="8.5" width="84" height="6.7" fill="var(--stripe-grey)"/>
        </pattern>
      </defs>
      <rect width="84" height="677" fill="url(#band-stripes)"/>
    </svg>
    <div class="card__info">
      <div class="brand-name">Lumawerks</div>
      <h1 class="person-name" style="font-weight:400">Darren Holtzmann</h1>
      <p class="person-role">designer</p>
      <p class="tagline">Custom Made Designer Furniture</p>
      <address class="address">
        18 Wexbury Rd<br>
        Kelston, Auckland<br>
        New Zealand 0712
      </address>
    </div>
  </div>
</body>
</html>
```